Marketing materials for Nimbletech company
trifolds, sign, and magnet
Thank you everyone for your submissions! They were all wonderful.
draft #18 is great - we will spend some time to more carefully review it and give some specific feedback later today. Thanks again
regarding draft #13 and draft #12, these are what we are looking for. The dark photo with the people we would like to go though. We are a small company and don't want to misrepresent that.
We are would use draft #12 for commercial services and draft #13 for residential. Is there anything that could be done to make them slightly different from each other inside though? If not, I'm sure we will find some content to fit - but if someone took one of each brochure, I don't want them to look identical other than the front and color. Maybe even just a different image in the middle of draft #12 where the laptop/wrench image is? Anyway, awesome work!
regarding draft #11, I prefer this to draft #5. Just something doesn't quite fit for me - I'll try to come up with something more specific. Thanks though - this is currently our 2nd favorite
regarding draft #10, I hadn't thought about it before, but I love how one brochure uses mostly blue, and the other uses mostly orange. I also like the flow of both of these. I can't tell if they are tri-fold though. But if you were wondering if we'd like the idea - we do!
-Wade
Also, if it helps, you can checkout what we liked / didn't like in our ongoing stationery / business card content!
Our contest link is: http://www.quintaloft.net/contests/business-card-template-company-stationery
so I will try to be more specific to assist until the unveil it - but bear with me, this is not my area :-) So blue and orange are preferable. Less gradients are better. Curves and circles that flow across the entire front or back for the residential tri-fold connecting the content areas is preferable. Same idea, but with straight angled boxes seems to be what I like on the business tri-fold. Pictures seem more important on the business one (based on existing designs that we have seen), residential can use illustrations in place of pictures. That's what I've got for now!
I just noticed this project is listed as "veiled" even though I did not choose to do so, so I apologize if you can not see the comparisons I am making between each others designs. I will contact support to fix this.
regarding draft #1, thank you for the submission. While I will make some remarks about what I would like to see in the layout, this set of documents is very much along the lines of what I am looking for. The 8.5x11 represents the content of the tri-fold and the magnet has room for a 1" x 3" label. I also like the use of blue! There is something plain about the actual layout though, in comparison to the angles used in draft #4 business tri-fold or curves of draft #4 residential. Thanks again for the submission!
regarding draft #2, I really like the use of our colors and thank you for the submission! I would like more photos as opposed to graphics such as the "help / mouse" or "laptop with stethoscope". I felt the overall feel was very busy and took up a lot of space without providing much room for content. I did like the use of our logo, but I'm ok with it taking up less room in exchange for a really clean look.
regarding draft #3, I like the nerdy magnet guy, but needs room for a 1"x3" thermal label and more room for our name / contact info
regarding draft #4, I like the look of the business tri-fold more than that of the residential. The graphic for the back especially. I think the colors on the residential need to be brighter and more playful. I think the idea of the business tri-fold having more straight lines and sharp angles, while the residential has more curves is great. Just the colors and overall look don't appeal to me. While neither of the magnets would fit a 1x3 label I LOVE how simple the magnet with our logo cutout looks - great idea!

```html
<!DOCTYPE html>
<html lang="en">
<head>
<meta charset="utf-8">
<title>Nimbletech trifold, cover stack and magnet</title>
<link href="https://fonts.googleapis.com/css2?family=Open+Sans:wght@400;600;700&display=swap" rel="stylesheet">
<style>
:root{
  --blue:#1f6fb7;
  --orange:#f28c1e;
  --text:#555;
  --white:#fff;
  --photo-a:#c7ccd2;
  --photo-b:#8d96a1;
}
*{box-sizing:border-box;margin:0;padding:0}
html,body{width:1200px;height:636px;overflow:hidden;background:var(--white);font-family:"Open Sans",Arial,sans-serif;color:var(--text)}
.canvas{position:relative;width:1200px;height:636px}

/* trifold inside spread */
.trifold{position:absolute;left:7px;top:7px;width:756px;height:466px;display:flex;box-shadow:0 1px 4px rgba(0,0,0,.25)}
.panel{position:relative;width:252px;height:100%;overflow:hidden;background:var(--white)}
.panel + .panel{border-left:1px solid #ddd}
.panel-heading{position:absolute;font-size:12px;font-weight:700;color:var(--blue)}

.panel-about{background:linear-gradient(90deg,#e2e2e2 0,#f6f6f6 40%,#fff 100%)}
.panel-about .about-heading{left:14px;top:18px}
.panel-about .testimonials-heading{left:14px;top:262px}
.about-text{position:absolute;left:14px;top:40px;width:170px;font-size:8.5px;line-height:1.55}
.about-logo-bar{position:absolute;left:0;top:205px;width:120px;height:40px;background:var(--orange);display:flex;align-items:center;justify-content:center}
.testimonial{position:absolute;left:14px;width:224px;display:flex;gap:8px}
.testimonial-photo{width:38px;height:46px;flex:none;background:linear-gradient(160deg,var(--photo-a),var(--photo-b))}
.testimonial-quote{font-size:8px;line-height:1.5}
.testimonial-name{display:block;text-align:right;color:var(--orange);font-size:7.5px;margin-top:3px}

.services-photo{position:absolute;left:0;top:0;width:252px;height:260px;background:radial-gradient(ellipse at 30% 45%,#d4d7db 0,#ebedef 55%,#fff 85%)}
.panel-services .services-heading{left:30px;top:16px}
.service-list{position:absolute;left:30px;top:42px;list-style:none;font-size:9px;line-height:2.2;color:#444}
.service-list li{display:flex;align-items:center;gap:8px}
.service-list svg{width:10px;height:10px}
.contact-block{position:absolute;left:30px;top:340px;font-size:8px;line-height:1.7;font-style:normal}
.contact-web{position:absolute;left:0;bottom:18px;width:100%;text-align:center;font-size:8px;color:var(--blue)}

.panel-cover .cover-logo{position:absolute;right:18px;top:22px}
.cover-photo{position:absolute;left:30px;top:72px;width:192px;height:170px;background:linear-gradient(180deg,#e7eaee,var(--photo-a) 60%,var(--photo-b))}
.cover-tagline{position:absolute;right:22px;top:258px;text-align:right;color:var(--blue)}
.cover-tagline strong{display:block;font-size:19px;font-weight:700;line-height:1.1}
.cover-tagline span{font-size:13px}

/* logo wordmark */
.wordmark{display:flex;align-items:center;gap:6px;font-weight:700;color:var(--blue);line-height:1}
.wordmark .mark-square{width:12px;height:12px;background:var(--orange)}
.wordmark .wordmark-name{font-size:17px}
.wordmark-sub{display:block;font-size:6.5px;color:var(--text);font-weight:400;margin-bottom:2px;text-align:right}
.wordmark-light{color:var(--white)}
.wordmark-light .wordmark-name{font-size:14px}

/* stack of covers */
.cover-stack{position:absolute;left:0;top:0;width:1200px;height:636px}
.sheet{position:absolute;left:936px;top:144px;width:250px;height:396px;background:var(--white);box-shadow:0 1px 4px rgba(0,0,0,.3);transform-origin:0 100%}
.sheet-back-4{transform:rotate(-20deg)}
.sheet-back-3{transform:rotate(-15deg)}
.sheet-back-2{transform:rotate(-10deg)}
.sheet-back-1{transform:rotate(-5deg)}
.sheet-back{background:linear-gradient(180deg,#fff 0,#fff 50%,var(--blue) 50%)}
.sheet-front{overflow:hidden}
.sheet-front .cover-logo{position:absolute;right:14px;top:14px}
.front-photo{position:absolute;left:18px;top:52px;width:214px;height:150px;background:linear-gradient(180deg,#e7eaee,var(--photo-a) 60%,var(--photo-b))}
.front-band{position:absolute;left:0;top:192px;width:250px;height:204px}
.front-tagline{position:absolute;right:14px;top:226px;text-align:right;color:var(--orange)}
.front-tagline strong{display:block;font-size:19px;font-weight:700;line-height:1.1}
.front-tagline span{font-size:12px}
.front-contact{position:absolute;right:14px;top:290px;text-align:right;font-size:6.5px;line-height:1.6;color:var(--white)}
.front-web{position:absolute;left:0;bottom:8px;width:100%;text-align:center;font-size:6.5px;color:var(--white)}

/* magnet */
.magnet{position:absolute;left:925px;top:557px;width:265px;height:72px;display:flex;box-shadow:0 1px 4px rgba(0,0,0,.3);border-radius:4px;overflow:hidden}
.magnet-brand{width:125px;background:var(--orange);display:flex;align-items:center;justify-content:center}
.magnet-call{flex:1;background:var(--white);padding:14px 10px;text-align:right}
.magnet-call strong{display:block;color:var(--blue);font-size:13px;font-weight:700}
.magnet-call span{display:block;color:var(--orange);font-size:8.5px;font-weight:600;line-height:1.4}
</style>
</head>
<body>
<div class="canvas">

  <section class="trifold">
    <div class="panel panel-about">
      <h2 class="panel-heading about-heading">About Us</h2>
      <p class="about-text">Nimbletech is a family run team fixing home and office computers since day one. We keep your machines fast, safe and working so you can get on with the things that matter most to you every day.</p>
      <div class="about-logo-bar">
        <div class="wordmark wordmark-light"><span class="wordmark-name">Nimbletech</span></div>
      </div>
      <h2 class="panel-heading testimonials-heading">What People Says</h2>
      <div class="testimonial" style="top:286px">
        <div class="testimonial-photo" role="img" aria-label="Portrait photo of a customer"></div>
        <p class="testimonial-quote">Quick, friendly and honest. My laptop was back the next day and running better than new.<span class="testimonial-name">Dana Ruiz, Homeowner</span></p>
      </div>
      <div class="testimonial" style="top:362px">
        <div class="testimonial-photo" role="img" aria-label="Portrait photo of a customer"></div>
        <p class="testimonial-quote">They saved all our office files after a crash. Clear prices and no fuss at all.<span class="testimonial-name">Paul Okafor, Office Manager</span></p>
      </div>
    </div>

    <div class="panel panel-services">
      <div class="services-photo" role="img" aria-label="Faded photo of a desktop computer"></div>
      <h2 class="panel-heading services-heading">Our Services</h2>
      <ul class="service-list">
        <li><svg viewBox="0 0 10 10"><path d="M1 5l3 3 5-7" fill="none" stroke="#f28c1e" stroke-width="1.8"/></svg>Virus &amp; Spyware</li>
        <li><svg viewBox="0 0 10 10"><path d="M1 5l3 3 5-7" fill="none" stroke="#f28c1e" stroke-width="1.8"/></svg>Remove Reinstalling</li>
        <li><svg viewBox="0 0 10 10"><path d="M1 5l3 3 5-7" fill="none" stroke="#f28c1e" stroke-width="1.8"/></svg>Operating Systems</li>
        <li><svg viewBox="0 0 10 10"><path d="M1 5l3 3 5-7" fill="none" stroke="#f28c1e" stroke-width="1.8"/></svg>Data back up and Recovery</li>
        <li><svg viewBox="0 0 10 10"><path d="M1 5l3 3 5-7" fill="none" stroke="#f28c1e" stroke-width="1.8"/></svg>Laptop DC jack Repair</li>
        <li><svg viewBox="0 0 10 10"><path d="M1 5l3 3 5-7" fill="none" stroke="#f28c1e" stroke-width="1.8"/></svg>Laptop Screen repair</li>
      </ul>
      <address class="contact-block">
        101 Harbor St, Unit 4<br>
        Lakeview, ON 00000<br>
        (000) 000-0000<br>
        (000) 000-0001<br>
        help@nimbletech.example
      </address>
      <p class="contact-web">www.nimbletech.example</p>
    </div>

    <div class="panel panel-cover">
      <div class="cover-logo">
        <span class="wordmark-sub">Your local</span>
        <div class="wordmark"><span class="mark-square"></span><span class="wordmark-name">Nimbletech</span></div>
      </div>
      <div class="cover-photo" role="img" aria-label="Photo of a smiling technician in shirt and tie with arms crossed in front of computers"></div>
      <p class="cover-tagline"><strong>leave behind</strong><span>for all PC's we repair</span></p>
    </div>
  </section>

  <section class="cover-stack">
    <div class="sheet sheet-back sheet-back-4"></div>
    <div class="sheet sheet-back sheet-back-3"></div>
    <div class="sheet sheet-back sheet-back-2"></div>
    <div class="sheet sheet-back sheet-back-1"></div>
    <div class="sheet sheet-front">
      <div class="cover-logo">
        <span class="wordmark-sub">Your local</span>
        <div class="wordmark"><span class="mark-square"></span><span class="wordmark-name">Nimbletech</span></div>
      </div>
      <div class="front-photo" role="img" aria-label="Photo of a smiling technician in shirt and tie with arms crossed in front of computers"></div>
      <svg class="front-band" viewBox="0 0 250 204" preserveAspectRatio="none">
        <path d="M0 26 Q125 -8 250 18 L250 204 L0 204 Z" fill="#1f6fb7"/>
        <path d="M0 26 Q125 -8 250 18" fill="none" stroke="#f28c1e" stroke-width="3"/>
      </svg>
      <p class="front-tagline"><strong>leave behind</strong><span>for all PC's we repair</span></p>
      <p class="front-contact">101 Harbor St, Unit 4<br>Lakeview, ON 00000<br>(000) 000-0000<br>help@nimbletech.example</p>
      <p class="front-web">www.nimbletech.example</p>
    </div>
  </section>

  <section class="magnet">
    <div class="magnet-brand">
      <div class="wordmark wordmark-light"><span class="wordmark-name">Nimbletech</span></div>
    </div>
    <div class="magnet-call">
      <strong>CALL NOW</strong>
      <span>(000) 000-0000</span>
      <span>(000) 000-0001</span>
    </div>
  </section>

</div>
</body>
</html>
```